Subscription Box Company Needs a Boxwren Box Design

WE NEED 5 sides of a 10" x 4" x 8" box designed.
Not one entire design, should be simple with 5 images or designs within one project. Visit boxwren.com to see what we mean.

What we need:
We send our subscribers new and unique products and we want a box that conveys professional yet fun and exciting feelings. We want our logo (attached) and our website (zorvat.com) listed somewhere. The rest is up to you!

WHAT WE NEED FROM YOU:
Go to boxwren.com and select their mailer box, then select their 10" x 8" x 4" mailer box with a white background. We need your design to be able to upload on each side of the box - so we can just take your design and upload it on their website. That simple!

Please follow the directions above!

From Boxwren :

Color Settings

Your artwork can be either CMYK or RGB, but we would highly encourage you to convert your images into CMYK before making your order. This allows you to ‘soft-proof’ your images on screen and see how the colors will look. If you supply your images in RGB they will be automatically converted to CMYK. RGB colors may appear duller or desaturated when printed (and we’re sure you don’t want that).

Design Formats

Any non-photographic content (including graphics and text) are best sent to us as vector based PDFs or Adobe Illustrator (.ai) files. These make your lines crisp and clear.

Please make sure there are no cut or crop lines, all transparencies have been flattened, and any fonts are embedded (or outlined) before saving your designs. To do that in Adobe Illustrator, select all text and choose Type > Create Outlines.

Design Typography, Text and Line Art

Just a few *important* points:

Text should be at least 14pt - regardless of how it looks on screen, any smaller and it won’t print well on corrugate.
Try to keep text in bold weights and colors.
If any of your lines are in a solid or dark color, make sure they’re no thinner than 2pt.
All fonts should be outlined/vectorized.

Industry/Entity Type

It Company

Colors
0592cd
ffffff
33a6d7
85cae6
cee9f5

Requirements
Must have
• Our logo, and our website zorvat.com listed somewhere.
Nice to have
• Anything!
Should not have
• Nothing to masculine or feminine, we want it gender neutral.

```html
<!DOCTYPE html>
<html lang="en">
<head>
<meta charset="utf-8">
<title>Zorvat Mailer Box – Panel Layout</title>
<link rel="stylesheet" href="https://fonts.googleapis.com/css2?family=Open+Sans:wght@400;600&display=swap">
<style>
  :root {
    --sheet-bg: #ffffff;
    --label-red: #e8121c;
    --brand-blue: #1f9ad2;
    --url-blue: #2a86b8;
    --sky-deep: #5f95cf;
    --sky-mid: #85cae6;
    --sky-light: #cee9f5;
    --sky-white: #f4fafd;
  }
  * { margin: 0; padding: 0; box-sizing: border-box; }
  html, body {
    width: 1102px;
    height: 1200px;
    overflow: hidden;
    background: var(--sheet-bg);
    font-family: "Open Sans", sans-serif;
  }
  .sheet {
    position: relative;
    width: 1102px;
    height: 1200px;
  }
  .side-label {
    position: absolute;
    color: var(--label-red);
    font-size: 32px;
    font-weight: 400;
    letter-spacing: 1px;
    line-height: 1;
    white-space: nowrap;
  }
  .side-label--top { left: 217px; top: 0; }
  .side-label--sides { left: 654px; top: 80px; }
  .side-label--back { left: 788px; top: 545px; }
  .side-label--front { left: 499px; top: 990px; }

  .panel {
    position: absolute;
    overflow: hidden;
  }
  .panel-art {
    position: absolute;
    inset: 0;
    background:
      radial-gradient(ellipse at 12% 10%, var(--sky-deep) 0%, transparent 38%),
      radial-gradient(ellipse at 95% 55%, var(--sky-deep) 0%, transparent 30%),
      radial-gradient(ellipse at 45% 60%, var(--sky-white) 0%, transparent 45%),
      linear-gradient(160deg, var(--sky-mid) 0%, var(--sky-light) 55%, var(--sky-mid) 100%);
  }
  .panel--top { left: 15px; top: 33px; width: 524px; height: 419px; }
  .panel--sides { left: 564px; top: 146px; width: 522px; height: 208px; }
  .panel--back { left: 630px; top: 614px; width: 268px; height: 214px; }
  .panel--front { left: 33px; top: 918px; width: 436px; height: 217px; }

  .brand-lockup {
    position: absolute;
    text-align: center;
    transform: translateX(-50%);
    white-space: nowrap;
  }
  .brand-name {
    display: block;
    color: var(--brand-blue);
    font-weight: 600;
    line-height: 1;
  }
  .brand-url {
    display: block;
    color: var(--url-blue);
    font-weight: 400;
    letter-spacing: 1px;
  }
  .panel--top .brand-lockup { left: 268px; top: 140px; }
  .panel--top .brand-name { font-size: 92px; }
  .panel--top .brand-url { font-size: 31px; margin-top: 24px; }

  .panel--sides .brand-lockup { left: 264px; top: 60px; }
  .panel--sides .brand-name { font-size: 48px; }
  .panel--sides .brand-url { font-size: 18px; margin-top: 12px; }

  .panel--front .brand-lockup { left: 387px; top: 163px; }
  .panel--front .brand-name { font-size: 24px; }
  .panel--front .brand-url { font-size: 7px; margin-top: 5px; letter-spacing: 0.3px; }
</style>
</head>
<body>
<main class="sheet">
  <div class="side-label side-label--top">TOP</div>
  <section class="panel panel--top">
    <div class="panel-art" role="img" aria-label="Soft blue and white cloud sky texture"></div>
    <div class="brand-lockup">
      <span class="brand-name">zorvat</span>
      <span class="brand-url">WWW.ZORVAT.COM</span>
    </div>
  </section>

  <div class="side-label side-label--sides">LEFT AND RIGHT</div>
  <section class="panel panel--sides">
    <div class="panel-art" role="img" aria-label="Soft blue and white cloud sky texture"></div>
    <div class="brand-lockup">
      <span class="brand-name">zorvat</span>
      <span class="brand-url">WWW.ZORVAT.COM</span>
    </div>
  </section>

  <div class="side-label side-label--back">BACK</div>
  <section class="panel panel--back">
    <div class="panel-art" role="img" aria-label="Soft blue and white cloud sky texture"></div>
  </section>

  <section class="panel panel--front">
    <div class="panel-art" role="img" aria-label="Soft blue and white cloud sky texture"></div>
    <div class="brand-lockup">
      <span class="brand-name">zorvat</span>
      <span class="brand-url">WWW.ZORVAT.COM</span>
    </div>
  </section>
  <div class="side-label side-label--front">FRONT</div>
</main>
</body>
</html>
```